Business Card Design

We are a residential half way house for the addict ,the alcoholic and dual diagnosed in recovery.
i house both men and woman age 18+

Industry/Entity Type

Residential

```html
<!DOCTYPE html>
<html lang="en">
<head>
<meta charset="utf-8">
<title>Harborlight Family Sober House – Business Card</title>
<link href="https://fonts.googleapis.com/css2?family=Questrial&family=Montserrat:wght@700&display=swap" rel="stylesheet">
<style>
  :root {
    --teal: #1aa9ae;
    --teal-dark: #138d92;
    --grey-text: #7d7f82;
    --grey-light: #b3b5b8;
    --card: #ffffff;
    --stage: #e9ebec;
  }
  * { box-sizing: border-box; margin: 0; padding: 0; }
  html, body {
    width: 1200px; height: 1000px; overflow: hidden;
    background: var(--stage);
  }
  .business-card {
    position: absolute; left: 75px; top: 200px;
    width: 1050px; height: 600px;
    background: var(--card);
    border-radius: 42px;
    overflow: hidden;
    box-shadow: 0 8px 28px rgba(0,0,0,.12);
    font-family: "Questrial", sans-serif;
    color: var(--grey-text);
  }
  .card-band { position: absolute; inset: 0; }
  .brand {
    position: absolute; left: 0; right: 0; top: 40px;
    text-align: center;
  }
  .brand-mark {
    width: 96px; height: 96px; margin: 0 auto 18px;
    border-radius: 50%; background: var(--teal);
  }
  .brand-name {
    font-size: 42px; line-height: 1.05; color: var(--grey-text);
  }
  .brand-rule {
    position: absolute; top: 250px; height: 2px; background: var(--grey-light);
  }
  .brand-rule.left { left: 300px; width: 120px; }
  .brand-rule.right { left: 630px; width: 120px; }
  .owner {
    position: absolute; right: 500px; top: 290px; text-align: right;
  }
  .owner-name {
    font-family: "Montserrat", sans-serif; font-weight: 700;
    font-size: 34px; color: var(--teal);
  }
  .owner-role { font-size: 24px; margin-top: 2px; }
  .divider {
    position: absolute; left: 570px; top: 285px; width: 4px; height: 120px;
    background: var(--grey-light);
  }
  .contacts {
    position: absolute; left: 588px; top: 284px; list-style: none;
    font-size: 22px; line-height: 30px;
  }
  .contacts li { display: flex; align-items: center; gap: 10px; }
  .contacts svg { width: 20px; height: 20px; flex: none; }
  .address {
    position: absolute; left: 48px; top: 448px;
    display: flex; align-items: center; gap: 10px;
    font-size: 27px; color: var(--grey-light);
  }
  .address svg { width: 22px; height: 22px; }
  .tagline {
    position: absolute; right: 60px; top: 500px;
    font-size: 30px; color: #fff;
  }
</style>
</head>
<body>
  <div class="business-card">
    <svg class="card-band" viewBox="0 0 1050 600" aria-hidden="true">
      <path d="M0 520 C 300 520, 700 480, 1050 400 L1050 600 L0 600 Z" fill="var(--teal)"/>
      <path d="M0 560 C 350 560, 750 520, 1050 450 L1050 600 L0 600 Z" fill="var(--teal-dark)" opacity=".35"/>
    </svg>

    <header class="brand">
      <div class="brand-mark"></div>
      <div class="brand-name">Harborlight Family<br>Sober House Inc</div>
    </header>
    <span class="brand-rule left"></span>
    <span class="brand-rule right"></span>

    <div class="owner">
      <div class="owner-name">Dana Whitfield</div>
      <div class="owner-role">Owner</div>
    </div>
    <span class="divider"></span>

    <ul class="contacts">
      <li><svg viewBox="0 0 20 20"><rect width="20" height="20" rx="5" fill="var(--teal)"/><path d="M6 5h3l1 3-2 1a7 7 0 0 0 3 3l1-2 3 1v3c-6 0-9-3-9-9z" fill="#fff"/></svg>(555) 010-0305</li>
      <li><svg viewBox="0 0 20 20"><rect width="20" height="20" rx="5" fill="var(--teal)"/><path d="M6 5h3l1 3-2 1a7 7 0 0 0 3 3l1-2 3 1v3c-6 0-9-3-9-9z" fill="#fff"/></svg>(555) 010-0306</li>
      <li><svg viewBox="0 0 20 20"><rect width="20" height="20" rx="5" fill="var(--teal)"/><rect x="7" y="4" width="6" height="12" rx="1" fill="#fff"/></svg>(555) 014-5536</li>
      <li><svg viewBox="0 0 20 20"><rect width="20" height="20" rx="5" fill="var(--teal)"/><rect x="4" y="6" width="12" height="8" fill="#fff"/><path d="M4 6l6 5 6-5" stroke="var(--teal)" fill="none"/></svg>danawhitfield@example.com</li>
    </ul>

    <div class="address">4820 Palm Grove Rd. Bayview,Fla 3346
      <svg viewBox="0 0 20 20"><rect width="20" height="20" rx="5" fill="var(--teal)"/><path d="M10 4a4 4 0 0 1 4 4c0 3-4 8-4 8s-4-5-4-8a4 4 0 0 1 4-4z" fill="#fff"/><circle cx="10" cy="8" r="1.5" fill="var(--teal)"/></svg>
    </div>

    <div class="tagline">Your Sobriety is our Priority</div>
  </div>
</body>
</html>
```